Digital Price Menus for Detail Shop

I am looking to have digital menus for my detail shop. I have 3 55-inch TVs (see pictures) on how they are situated on the wall for my front desk area. They will be vertical, not horizontal.

Color pallet I am looking for is black and gold, with some accent colors if applicable. I would like black background with some sort of design in it in such a way it looks faint or ghosted in the background ... i.e., honeycomb, splatter, etc. A boarder is optional.

Needs to be designed well, organized well and easy to read for customers walking in.

the each document is for each TV, Interior, Exterior and Ceramic Coatings

Company logo files included. would like my logos on them as well

Target Market(s)

Customers walking in to my shop, easy to read and understand

Industry/Entity Type

Car wash, Detailing

Colors

Designer to choose only greyscale colors for use in the design.

Requirements
Nice to have
• Professional Look
Should not have
• tacky look

```html
<!DOCTYPE html>
<html lang="en">
<head>
<meta charset="utf-8">
<title>Detail Shop Digital Price Menus</title>
<link href="https://fonts.googleapis.com/css2?family=Bebas+Neue&family=Roboto:wght@400;500&display=swap" rel="stylesheet">
<style>
:root{
  --paper:#ffffff;
  --screen:#050505;
  --card:#000000;
  --line:#8a8a8a;
  --gold:#f2c21b;
  --text:#e6e6e6;
  --muted:#b5b5b5;
  --alert:#e0261d;
}
*{margin:0;padding:0;box-sizing:border-box}
html,body{width:1200px;height:708px;overflow:hidden;background:var(--paper)}
body{position:relative;font-family:'Roboto',Arial,sans-serif;color:var(--text)}
.screen{position:absolute;top:13px;width:384px;height:683px;overflow:hidden;
  background:radial-gradient(ellipse 75% 30% at 50% 52%,#3a3a3a 0%,#1b1b1b 45%,var(--screen) 80%)}
.screen--exterior{left:13px}
.screen--interior{left:410px}
.screen--ceramic{left:803px}
.backdrop{position:absolute;inset:0;background:linear-gradient(180deg,rgba(0,0,0,.85) 0%,rgba(0,0,0,0) 35%,rgba(0,0,0,0) 70%,rgba(0,0,0,.9) 100%)}
.title-tab{position:absolute;border:1px solid var(--line);border-radius:6px;background:var(--card);display:flex;align-items:center;justify-content:center}
.title-tab h1{font-family:'Bebas Neue',Impact,sans-serif;font-weight:400;color:var(--gold);font-size:27px;letter-spacing:.5px;white-space:nowrap;transform:rotate(-90deg);line-height:1}
.card{position:absolute;border:1px solid var(--line);border-radius:7px;background:var(--card);padding:7px 9px}
.card h2{font-family:'Bebas Neue',Impact,sans-serif;font-weight:400;color:var(--gold);font-size:12.5px;text-align:center;line-height:1;margin:6px 0 4px}
.card h2:first-child{margin-top:3px}
.card p{font-size:5.2px;line-height:1.28;color:var(--text)}
.card p + p{margin-top:5px}
.fine{font-size:3.6px;color:var(--muted)}
.price{display:flex;align-items:baseline;font-family:'Bebas Neue',Impact,sans-serif;color:var(--gold);font-size:8.2px;line-height:1;margin-top:3px}
.price .leader{flex:1;border-bottom:1px dotted #777;margin:0 3px;transform:translateY(-1px)}
.price .unit{font-family:'Roboto',Arial,sans-serif;font-size:3.6px;color:var(--text);margin-right:3px}
.price.stacked .unit{line-height:1.5}
.addon{margin-top:8px}
.addon:first-of-type{margin-top:4px}
.addon p{margin-top:2px}
.alert{color:var(--alert)}
</style>
</head>
<body>

<section class="screen screen--exterior">
  <div class="backdrop" role="img" aria-label="Faint honeycomb texture and ghosted shop emblem glowing on black"></div>
  <div class="title-tab" style="left:57px;top:17px;width:46px;height:310px"><h1>Exterior Detailing Packages</h1></div>

  <div class="card" style="left:113px;top:19px;width:191px;height:320px">
    <h2>Hand Wash</h2>
    <p>Presoak, foam bath, bug remover, wheel detail, wheel wells cleaned, tires dressed, exterior glass cleaned, blow dry &nbsp;(+add spray wax $20)</p>
    <div class="price"><span>Car</span><span class="leader"></span><span>$50</span></div>
    <div class="price"><span>Truck/SUV</span><span class="leader"></span><span>$60+</span></div>
    <h2>Complete Exterior Detail</h2>
    <p>Standard hand wash, iron decontamination, clay bar treatment to remove environmental contamination (sap, tar, etc) tires, wheels, wheel wells cleaned and dressed, door jams, trunk lid, gas cap areas cleaned, exterior glass cleaned, black plastics dressed, Paint work is protected with a hand applied wax. <span class="fine">*DOES NOT REMOVE ANY PAINT DEFECTS*</span></p>
    <div class="price"><span>Car</span><span class="leader"></span><span>$180</span></div>
    <div class="price"><span>Truck/SUV</span><span class="leader"></span><span>$220</span></div>
    <h2>Paint Enhancement</h2>
    <p>Our paint protection package PLUS paint receives a one-step polish to deep clean the paint, reduce swirls and increases gloss, windshield is polished and protected with Glazorra, Paint work is protected with a Ceramic Sealant lasting up to 6 months.</p>
    <div class="price"><span>Car</span><span class="leader"></span><span>$350</span></div>
    <div class="price"><span>Truck/SUV</span><span class="leader"></span><span>$400</span></div>
    <h2>Paint Correction</h2>
    <p>Our paint enhancement PLUS paint receives a 2-step correction process to safely remove swirls, defects, and minor scratches, achieving 90% or better appearance.</p>
    <div class="price"><span>Car</span><span class="leader"></span><span>$500</span></div>
    <div class="price"><span>Truck/SUV</span><span class="leader"></span><span>$600+</span></div>
  </div>

  <div class="card" style="left:113px;top:352px;width:191px;height:86px">
    <h2 style="margin-top:10px">Restorative Detail</h2>
    <p style="margin-top:6px">Have an old, classic or just plain oddball car? Some circumstances like single stage, vintage or patina paint doesn't fall under any of our packages but we can service anything! This type of job will require a consultation to go over the vehicle thoroughly and set a plan of action.</p>
  </div>

  <div class="card" style="left:113px;top:452px;width:191px;height:215px">
    <h2 style="margin-top:10px;margin-bottom:8px">Exterior Add-Ons</h2>
    <div class="price addon"><span>Headlight Restoration</span><span class="leader"></span><span>$100+</span></div>
    <div class="price addon"><span>Plastic Trim Restoration</span><span class="leader"></span><span>$50+</span></div>
    <div class="price addon"><span>Water Spot Removal</span><span class="leader"></span><span>$50+</span></div>
    <div class="price addon"><span>Scratch Removal</span><span class="leader"></span><span class="unit">*Consultation required</span></div>
    <div class="price addon"><span>Complete Wheel Detail</span><span class="leader"></span><span>$150</span></div>
    <p>Wheels off, deep cleaned and protected inside and out, reinstalled and torqued to factory spec.</p>
    <div class="price addon stacked"><span>Verrano Window Protection</span><span class="leader"></span><span class="unit">*windshield<br>*all windows</span><span>$100<br>$150</span></div>
    <p>Glass surface(s) prepped and polished. 3-year warrantied protection plan with quarterly maintenance for free.</p>
    <div class="price addon"><span>Engine Bay Cleaning</span><span class="leader"></span><span>$50+</span></div>
    <p>Degreased and dressed. *Waiver must be signed and completed prior to work being performed.</p>
  </div>
</section>

<section class="screen screen--interior">
  <div class="backdrop" role="img" aria-label="Faint honeycomb texture and ghosted shop emblem glowing on black"></div>
  <div class="title-tab" style="left:57px;top:24px;width:46px;height:276px"><h1>Interior Detail Packages</h1></div>

  <div class="card" style="left:113px;top:24px;width:192px;height:337px">
    <h2 style="margin-top:10px">Basic Interior Clean</h2>
    <p>Full vacuum of carpet, seats, upholstery, Floormats extracted and steam cleaned, dash/doors wiped and dressed, interior glass surfaces cleaned, center console steam cleaned</p>
    <div class="price" style="margin-top:5px"><span>Car/Truck/SUV</span><span class="leader"></span><span>$100+</span></div>
    <h2 style="margin-top:9px">Deluxe Interior Clean</h2>
    <p>Basic Interior Package + Full steam clean and shampoo of all interior carpet and seats, leather is gently steamed and scrubbed lightly, dash/doors/vents are dusted and dressed, steering wheel and controls are deep cleaned and dressed. Headliner/visors are lightly cleaned <span class="fine">*Heavily soiled interiors that exceed a Deluxe Package will be charged extra*</span></p>
    <div class="price" style="margin-top:5px"><span>Car/Truck/SUV</span><span class="leader"></span><span>$200+</span></div>
    <h2 style="margin-top:9px">Deep Leather<br>Cleaning &amp; Conditioning</h2>
    <p>Premium Leather Conditioning Treatment + Basic Interior Package + Full steam clean and shampoo of all interior carpet and seats, leather is gently steamed and scrubbed lightly, dash/doors/vents are dusted and dressed, steering wheel and controls are deep cleaned and dressed. Headliner/visors are lightly cleaned <span class="fine">*Heavily soiled interiors that exceed a Deluxe Package will be charged extra*</span></p>
    <div class="price" style="margin-top:5px"><span>Car/Truck/SUV</span><span class="leader"></span><span class="unit">*per row</span><span>$100</span></div>
    <h2 style="margin-top:9px">Biohazard Cleaning</h2>
    <p>Basic Interior Package + Full steam clean and shampoo of all interior carpet and seats, leather is gently steamed and scrubbed lightly, dash/doors/vents are dusted and dressed, steering wheel and controls are deep cleaned and dressed. Headliner/visors are lightly cleaned <span class="fine">*Heavily soiled interiors that exceed a Deluxe Package will be charged extra*</span> + Plus Deluxe Interior Package</p>
    <div class="price" style="margin-top:5px"><span>Car/Truck/SUV</span><span class="leader"></span><span>$350</span></div>
  </div>

  <div class="card" style="left:113px;top:374px;width:192px;height:104px;padding-top:13px">
    <div class="price"><span>Fabric Guard</span><span class="leader"></span><span class="unit">*per row</span><span>$50+</span></div>
    <p style="margin-top:3px">Carpet and Fabric upholstery sprayed for stain and waterproofing.</p>
    <div class="price" style="margin-top:8px"><span>Ozone Treatment for Odors</span><span class="leader"></span><span>$50</span></div>
    <p style="margin-top:3px">Used to remove musty, smokey odors. Add to any packages.</p>
    <div class="price" style="margin-top:8px"><span>Excessive Pet Hair Removal</span><span class="leader"></span><span class="unit">10% Surcharge</span></div>
    <div class="price" style="margin-top:8px"><span>Trunk Area Detail</span><span class="leader"></span><span>$50+</span></div>
  </div>

  <div class="card" style="left:113px;top:496px;width:192px;height:107px">
    <h2 style="margin-top:12px;margin-bottom:8px">Reminder</h2>
    <p>As a reminder, we would appreciate all personal items be removed from interior.</p>
    <p>There may be instances were stains and pet hair are not fully removed, please understand we will do our best to remove as much as possible.</p>
    <p>Please see terms and conditions <span class="alert">(insert terms and conditions link)</span></p>
  </div>
</section>

<section class="screen screen--ceramic">
  <div class="backdrop" role="img" aria-label="Faint honeycomb texture and ghosted shop emblem glowing on black"></div>
  <div class="title-tab" style="left:56px;top:24px;width:47px;height:192px"><h1>Ceramic Coatings</h1></div>

  <div class="card" style="left:113px;top:24px;width:193px;height:192px;padding-top:10px">
    <p>All ceramic coating packages start with a Paint enhancement package. The 1 step polish will improve the appearance of blemishes, light marring and scratching 50-70%. On new cars it will reach up to 95%+ improvement. A full paint correction can be added for an additional cost. Day of pick up, a Sealant is applied to all coated surfaces to help with the curing process.</p>
    <p>Not every customer has the same goals when it comes to coatings so we have developed 3 different levels to choose from depending on your wants and needs and budget.</p>
    <div class="price" style="margin-top:12px"><span>1 Year Coating</span><span class="leader"></span><span>$500</span></div>
    <p style="margin-top:3px">Applied to all painted surfaces, provides up to 12months of durability. Add a second layer for $600 more for 18-24 months of protection.</p>
    <div class="price" style="margin-top:8px"><span>3 Year Coating</span><span class="leader"></span><span>$800</span></div>
    <p style="margin-top:3px">Applied to all painted surfaces, provides up to 36 months of durability.</p>
    <div class="price" style="margin-top:8px"><span>6 Year Coating</span><span class="leader"></span><span>$1000</span></div>
    <p style="margin-top:3px">Warrantied paint coating, applied to all painted surfaces, provides up to 60 months of durability.</p>
  </div>

  <div class="card" style="left:113px;top:229px;width:193px;height:64px">
    <h2 style="margin-top:8px;margin-bottom:5px">Note</h2>
    <p>Durability is directly related to the proper maintenance of the coatings.</p>
  </div>

  <div class="card" style="left:113px;top:306px;width:193px;height:113px;padding-top:13px">
    <div class="price"><span>Glass Ceramic Coating</span><span class="leader"></span><span>$100+</span></div>
    <div class="price" style="margin-top:9px"><span>Wheel Face Coating</span><span class="leader"></span><span class="unit">*per wheel</span><span>$30+</span></div>
    <p style="margin-top:3px">Wheel face coated with one layer of ceramic giving you up to 9-12 months of protection. 2 layers will yield 18+ of protection. *Raw aluminum wheels CAN NOT be coated.</p>
    <div class="price" style="margin-top:8px"><span>Wheel Off Coating</span><span class="leader"></span><span>$250+</span></div>
    <p style="margin-top:3px">Wheel coating package + durable industrial coating on barrels of wheels and if applicable, calipers and suspension components.</p>
  </div>
</section>

</body>
</html>
```